依頼詳細
レスポンシブウェブデザインを意識したデザインでお願いします。
参考URL
https://morisato-koubou.jp/

デザインに関しては、添付してあるデザインレイアウトシートを基にお願いします。

まずはパソコンサイトのデザインをお願いします。
当選後、スマホデザインをお願いします。

既存のテンプレートを使う場合は
テンプレート名を下記のような記載を提案の中にいれてください。
例:WordpressテーマはKandoria、デザインスキンは無料のHLM2019 RX4(http://kandoria.com/ex_plugin/hlmnagoya2019_rx4/)をベースにデザインいたしました。
など

素材となる写真は現在、撮影中ですので、一旦他のサイトや参考URLの写真をサンプルとして入れてください。(サンプルなどの表記をお願いします)
また、購入が必要な写真などを利用した場合は、Pelmora Stock(https://stock.pelmora.com/jp/)からファイル番号と価格を教えてください。
ページ数
1ページ
希望イメージ
シンプル 複雑
単色 カラフル
暗い 明るい
日常 高級
遊び心 厳粛
未来的 伝統的
女性的 男性的
希望する色
茶系、緑系
納品ファイル
• イラストレーター形式 (.ai)
• フォトショップ形式 (.psd)
• PNG形式 (.png)
補足説明
上記のいずれか1つ。アウトラインありとなしの2つ。

クライアントのイメージ通りでした。

たくさんのご提案ありがとうございました。
次回もぜひ、よろしくお願い致します。

```html
<!DOCTYPE html>
<html lang="ja">
<head>
<meta charset="utf-8">
<title>株式会社ミドリエ</title>
<link rel="stylesheet" href="https://fonts.googleapis.com/css2?family=Noto+Sans+JP:wght@400;500;700&family=Noto+Serif+JP:wght@400;500;700&display=swap">
<style>
:root{
  --green:#5f8f33;
  --green-dark:#4a7426;
  --brown:#7a5a34;
  --text:#4a4036;
  --muted:#8a8074;
  --line:#ddd5c8;
  --paper:#faf7f1;
  --wood-light:#efe4d0;
  --wood:#d9c19a;
  --gray-bg:#f1efeb;
  --white:#ffffff;
}
*{box-sizing:border-box;margin:0;padding:0}
html,body{width:1200px;height:3644px;overflow:hidden}
body{font-family:"Noto Sans JP",sans-serif;color:var(--text);background:var(--white);font-size:12px;line-height:1.7}
section,header,footer{overflow:hidden}
.container{width:900px;margin:0 auto}

/* header */
.site-header{height:120px;background:var(--white);border-bottom:1px solid var(--line)}
.brand{display:flex;align-items:center;justify-content:center;gap:10px;padding-top:20px;height:62px}
.brand-mark{width:24px;height:24px;background:var(--green)}
.brand-name{font-family:"Noto Serif JP",serif;font-size:20px;font-weight:700;color:var(--text)}
.global-nav{display:flex;justify-content:center;margin-top:16px}
.global-nav a{font-size:13px;color:var(--text);text-decoration:none;padding:0 26px;border-left:1px solid var(--line)}
.global-nav a:last-child{border-right:1px solid var(--line)}

/* hero */
.hero{position:relative;height:480px}
.hero-photo{position:absolute;inset:0;background:linear-gradient(90deg,#9ab9d6 0%,#c9b48d 28%,#e9d3a8 50%,#d8c092 68%,#8fb25e 86%,#bcd68a 100%)}
.hero-copy{position:absolute;top:150px;left:0;right:0;text-align:center}
.hero-title{font-family:"Noto Serif JP",serif;font-size:42px;font-weight:700;color:var(--white);line-height:1.35;text-shadow:0 2px 8px rgba(60,40,20,.55)}
.hero-tags{display:flex;justify-content:center;gap:18px;margin-top:34px}
.hero-tags span{background:var(--green);color:var(--white);font-size:13px;font-weight:500;padding:8px 18px}

/* section heading */
.section-title{text-align:center;font-family:"Noto Serif JP",serif;font-size:22px;font-weight:500;color:var(--text);display:flex;align-items:center;justify-content:center;gap:16px}
.section-title::before,.section-title::after{content:"";width:60px;height:1px;background:var(--brown)}
.section-lead{text-align:center;font-size:12px;color:var(--muted);margin-top:10px}

/* strengths */
.strengths{height:540px;background:linear-gradient(180deg,var(--paper),var(--wood-light));padding-top:42px}
.strength-list{display:flex;gap:12px;margin-top:30px}
.strength-card{width:171px;background:var(--white)}
.strength-photo{height:110px}
.strength-body{padding:12px 10px 16px}
.strength-body h3{font-size:12px;color:var(--green-dark);font-weight:700;line-height:1.5;text-align:center;white-space:nowrap}
.strength-body p{font-size:11px;color:var(--muted);margin-top:8px}

/* business */
.business{height:780px;background:var(--white);padding-top:44px}
.business-grid{display:grid;grid-template-columns:440px 440px;gap:30px 20px;margin-top:34px}
.business-photo{height:230px;position:relative}
.business-label{position:absolute;right:28px;top:50%;transform:translateY(-50%);font-family:"Noto Serif JP",serif;font-size:44px;line-height:1.3;color:var(--white);text-shadow:0 1px 6px rgba(60,40,20,.5)}
.business-item:nth-child(1) .business-label{left:24px;right:auto;color:var(--brown);text-shadow:none}
.business-item p{font-size:12px;color:var(--muted);margin-top:12px}

/* works */
.works{height:400px;background:var(--paper);padding-top:36px}
.work-list{display:flex;gap:20px;margin-top:30px}
.work-item{width:210px}
.work-photo{height:190px}
.work-item p{font-size:11px;color:var(--muted);text-align:center;margin-top:8px;line-height:1.5}

/* news and blog */
.updates{height:520px;background:var(--gray-bg);padding-top:40px}
.updates-inner{display:flex;gap:20px}
.panel{width:440px;background:var(--white)}
.panel-head{background:var(--wood-light);font-family:"Noto Serif JP",serif;font-size:15px;text-align:center;padding:10px 0;color:var(--brown)}
.news-row{display:flex;gap:14px;padding:12px 16px;border-bottom:1px dotted var(--line);font-size:11px}
.news-date{color:var(--green-dark);width:84px;flex:none}
.more{text-align:right;padding:14px 16px}
.more a{display:inline-block;border:1px solid var(--line);padding:4px 14px;font-size:11px;color:var(--muted);text-decoration:none}
.blog-item{display:flex;gap:16px;padding:18px 16px;border-bottom:1px dotted var(--line)}
.blog-photo{width:120px;height:90px;flex:none}
.blog-item time{font-size:10px;color:var(--muted)}
.blog-item h4{font-size:14px;color:var(--text);font-weight:700}
.blog-item p{font-size:11px;color:var(--muted)}

/* faq */
.faq{height:340px;background:var(--white);padding-top:40px}
.faq-list{margin-top:30px}
.faq-item{margin-bottom:24px}
.faq-q{font-size:14px;font-weight:500;display:flex;gap:14px;align-items:baseline}
.faq-q b{font-family:"Noto Serif JP",serif;font-size:24px;color:var(--green)}
.faq-a{font-size:11px;color:var(--muted);padding-left:36px;margin-top:4px}

/* contact */
.contact{height:250px;position:relative;background:linear-gradient(90deg,var(--wood-light),#e6d3b2 40%,var(--wood-light));text-align:center;padding-top:48px}
.contact-tel{font-family:"Noto Serif JP",serif;font-size:36px;color:var(--brown);display:inline-flex;align-items:center;gap:12px}
.contact-tel small{font-size:16px}
.contact-info{font-size:11px;color:var(--muted);margin-top:4px}
.contact-btn{display:inline-block;margin-top:18px;border:1px solid var(--brown);background:var(--white);color:var(--brown);font-size:14px;padding:10px 56px;text-decoration:none}
.contact-photo{position:absolute;right:150px;bottom:30px;width:120px;height:90px}

/* footer */
.site-footer{height:214px;background:var(--white);text-align:center;padding-top:44px;border-top:4px solid var(--green)}
.site-footer .brand{padding-top:0;height:auto}
.copyright{font-size:11px;color:var(--muted);margin-top:30px}
</style>
</head>
<body>

<header class="site-header">
  <div class="brand"><span class="brand-mark"></span><span class="brand-name">株式会社ミドリエ</span></div>
  <nav class="global-nav">
    <a href="#">HOME</a><a href="#">弊社の強み</a><a href="#">事業案内</a><a href="#">加工事例・商品紹介</a><a href="#">会社案内</a><a href="#">よくある質問</a><a href="#">お問い合わせ</a>
  </nav>
</header>

<section class="hero">
  <div class="hero-photo" role="img" aria-label="木製あずまや、積み重ねた木材、芝生に置かれた木製オブジェの写真"></div>
  <div class="hero-copy">
    <h1 class="hero-title">お客様のあらゆるご要望に<br>お応えいたします</h1>
    <div class="hero-tags">
      <span>住宅部材・ショーケース用部材の加工・組立</span>
      <span>加工工場を有する加工品対応</span>
      <span>各種木材・集成材・合板等の一括受付</span>
    </div>
  </div>
</section>

<section class="strengths">
  <h2 class="section-title">弊社の強み</h2>
  <p class="section-lead">弊社の強みを紹介するテキストが入ります。弊社の強みを紹介するテキストが入ります。</p>
  <div class="container strength-list">
    <div class="strength-card"><div class="strength-photo" role="img" aria-label="住宅部材の写真" style="background:linear-gradient(135deg,#c79a63,#e7c99c)"></div><div class="strength-body"><h3>住宅部材<br>加工・組立</h3><p>説明テキストが入ります。説明テキストが入ります。</p></div></div>
    <div class="strength-card"><div class="strength-photo" role="img" aria-label="什器部材の写真" style="background:linear-gradient(135deg,#d8b98a,#f1e2c6)"></div><div class="strength-body"><h3>什器部材（ショーケース）<br>部材加工・組立</h3><p>説明テキストが入ります。説明テキストが入ります。</p></div></div>
    <div class="strength-card"><div class="strength-photo" role="img" aria-label="床パネルの写真" style="background:linear-gradient(135deg,#b58a58,#dcc199)"></div><div class="strength-body"><h3>床板<br>パネル加工</h3><p>説明テキストが入ります。説明テキストが入ります。</p></div></div>
    <div class="strength-card"><div class="strength-photo" role="img" aria-label="梱包資材の写真" style="background:linear-gradient(135deg,#9c8a72,#d2c3a8)"></div><div class="strength-body"><h3>梱包資材・梱包加工</h3><p>説明テキストが入ります。説明テキストが入ります。</p></div></div>
    <div class="strength-card"><div class="strength-photo" role="img" aria-label="木材加工品の写真" style="background:linear-gradient(135deg,#a87b4d,#d6b487)"></div><div class="strength-body"><h3>その他・加工品等</h3><p>説明テキストが入ります。説明テキストが入ります。</p></div></div>
  </div>
</section>

<section class="business">
  <h2 class="section-title">事業案内</h2>
  <div class="container business-grid">
    <div class="business-item"><div class="business-photo" role="img" aria-label="並べた木材の写真" style="background:linear-gradient(90deg,#f4ead8,#e6cfa6)"><span class="business-label">材料</span></div><p>説明テキストが入ります。説明テキストが入ります。説明テキストが入ります。説明テキストが入ります。</p></div>
    <div class="business-item"><div class="business-photo" role="img" aria-label="木材の加工・組立作業の写真" style="background:linear-gradient(90deg,#cfc6b8,#a89a86)"><span class="business-label">加工・組立</span></div><p>説明テキストが入ります。説明テキストが入ります。説明テキストが入ります。説明テキストが入ります。</p></div>
    <div class="business-item"><div class="business-photo" role="img" aria-label="工場の加工設備の写真" style="background:linear-gradient(90deg,#8f8678,#c9bfae)"><span class="business-label">設備</span></div><p>説明テキストが入ります。説明テキストが入ります。説明テキストが入ります。説明テキストが入ります。</p></div>
    <div class="business-item"><div class="business-photo" role="img" aria-label="オーダーメイドの木製看板の写真" style="background:linear-gradient(90deg,#6f8a4a,#c9a977)"><span class="business-label">オーダー<br>メイド</span></div><p>説明テキストが入ります。説明テキストが入ります。説明テキストが入ります。説明テキストが入ります。</p></div>
  </div>
</section>

<section class="works">
  <h2 class="section-title">加工事例・商品紹介</h2>
  <div class="container work-list">
    <div class="work-item"><div class="work-photo" role="img" aria-label="芝生に置かれた木製オブジェの写真" style="background:linear-gradient(180deg,#9bbb6a,#6e9440)"></div><p>木製オブジェ製作事例<br>サンプル</p></div>
    <div class="work-item"><div class="work-photo" role="img" aria-label="木製の看板の写真" style="background:linear-gradient(180deg,#c89a5c,#8a9a62)"></div><p>木製看板製作事例<br>サンプル</p></div>
    <div class="work-item"><div class="work-photo" role="img" aria-label="ようこその文字入り木製看板の写真" style="background:linear-gradient(180deg,#a58457,#e0c79b)"></div><p>木製看板製作事例<br>サンプル</p></div>
    <div class="work-item"><div class="work-photo" role="img" aria-label="木製の杭と標識の写真" style="background:linear-gradient(180deg,#e3e0d6,#c7b28a)"></div><p>木製標識製作事例<br>サンプル</p></div>
  </div>
</section>

<section class="updates">
  <div class="container updates-inner">
    <div class="panel">
      <h3 class="panel-head">お知らせ</h3>
      <div class="news-row"><span class="news-date">2019.00.00</span><span>お知らせのタイトルが入ります。お知らせのタイトルが入ります。</span></div>
      <div class="news-row"><span class="news-date">2019.00.00</span><span>お知らせのタイトルが入ります。</span></div>
      <div class="news-row"><span class="news-date">2019.00.00</span><span>お知らせのタイトルが入ります。お知らせのタイトルが入ります。</span></div>
      <div class="news-row"><span class="news-date">2019.00.00</span><span>お知らせのタイトルが入ります。</span></div>
      <div class="news-row"><span class="news-date">2019.00.00</span><span>お知らせのタイトルが入ります。お知らせのタイトルが入ります。</span></div>
      <div class="news-row"><span class="news-date">2019.00.00</span><span>お知らせのタイトルが入ります。</span></div>
      <div class="more"><a href="#">お知らせ一覧</a></div>
    </div>
    <div class="panel">
      <h3 class="panel-head">ブログ</h3>
      <div class="blog-item"><div class="blog-photo" role="img" aria-label="ブログ記事の木材写真" style="background:linear-gradient(135deg,#b99466,#e6d1ad)"></div><div><time>2019.00.00</time><h4>タイトルタイトル</h4><p>本文テキストが入ります。本文テキストが入ります。本文テキストが入ります。</p></div></div>
      <div class="blog-item"><div class="blog-photo" role="img" aria-label="ブログ記事の作業風景写真" style="background:linear-gradient(135deg,#8a8070,#cbbda4)"></div><div><time>2019.00.00</time><h4>タイトルタイトル</h4><p>本文テキストが入ります。本文テキストが入ります。本文テキストが入ります。</p></div></div>
      <div class="more"><a href="#">ブログ一覧</a></div>
    </div>
  </div>
</section>

<section class="faq">
  <h2 class="section-title">よくある質問</h2>
  <div class="container faq-list">
    <div class="faq-item"><p class="faq-q"><b>Q.</b>よくある質問のテキストが入ります。テキストが入ります。</p><p class="faq-a">回答のテキストが入ります。回答のテキストが入ります。回答のテキストが入ります。回答のテキストが入ります。</p></div>
    <div class="faq-item"><p class="faq-q"><b>Q.</b>よくある質問のテキストが入ります。テキストが入ります。</p><p class="faq-a">回答のテキストが入ります。回答のテキストが入ります。回答のテキストが入ります。回答のテキストが入ります。</p></div>
  </div>
</section>

<section class="contact">
  <p class="contact-tel"><small>TEL.</small>0276-55-2048</p>
  <p class="contact-info">〒000-0000 群馬県〇〇市〇〇町0-0　受付時間 8:00〜17:00</p>
  <a class="contact-btn" href="#">お問い合わせはこちら</a>
  <div class="contact-photo" role="img" aria-label="木製の小さなテーブルの写真" style="background:linear-gradient(180deg,#b88a55,#7a5a34)"></div>
</section>

<footer class="site-footer">
  <div class="brand"><span class="brand-mark"></span><span class="brand-name">株式会社ミドリエ</span></div>
  <p class="copyright">Copyright © 株式会社ミドリエ All Rights Reserved.</p>
</footer>

</body>
</html>
```